DATA PROTECTION OFFICER - GENERAL DATA PROTECTION REGULATION

Our network of companies is called : KTV (GDPR-DPO ORLAX).
It is sourced and based in Brussels, Belgium, hosting the EU institutions : designers and enforcers of the GDPR (https://portal.vantreximo.example/info/law/privacy-rules_en).
We are setting up connected, empowered and visionary-interconnected organizations in each country, region or city concerned by the GDPR.
We have developed unique pedagogical methods, programs, instruments (video, softwares,…) and visionary training skills – initially and on a continuous basis – for the DPO & GDPR consultants.
Our motto is : From Challenges to Opportunities.
Our yearning is : developing soulful teams, join forces & talents with our clients.
Our most wanted reward : let us astonish you!
We opt for the best available softwares on the market for project management, data analytics, GDPR compliance, DPO assistance and in general : customer relation and enhanced communication between project members.
We contribute to bringing Artificial Intelligence and Data-Driven Mindsets in enterprises.
We perceive the GDPR as the best opportunity an organization faces to value its “gold” (its data) and offer the solutions to transform them into real-life currencies and assets… MONEY .
I guess my comments need time to be integrated and I provided a lot of text too! I would particularly encourage RW (UK) to take the best out of his several proposals to mix them in the best ONE website! Offering me many graphic elements to use for all my posts/pages... I am a prolix writer :)
Target Market(s)
SME's business leaders, HR and Legal departments, read : https://www.dailyquorvent.example/article/us-cyber-gdpr-dpo/growth-of-the-privacy-officer-role-in-firms-idQX8TR2LM4
Industry/Entity Type
Legal
Coding
Coded - Design and coding required
Number of Pages Required
5+ page
Colors
Designer to choose colors to be used in the design.
Requirements
Must have
- A HUMAN APPROACH
- WE NEED TO SEE HUMANS AND NOT ONLY ROBOTS OR ELECTRONIC DEVICES.
- 1) The DPO/GDPR Logos of the companies:
- https://files.pelmora.example/sh/a1b2c3d4e5f6g7h/AAX9kLmNpQrStUvWxYz0AbCd?dl=0
- https://files.pelmora.example/sh/h7g6f5e4d3c2b1a/AAY8jKlMnOpQrStUvWxYzAbC?dl=0 et DPO : https://files.pelmora.example/sh/q2w3e4r5t6y7u8i/AAZ7hIjKlMnOpQrStUvWxY-z?dl=0
- OR :
- https://files.pelmora.example/sh/z9x8c7v6b5n4m3l/AAW6gHiJkLmNoPqRsTuVwXyZ?dl=0
- AND :
- https://corvilanto.teamdrive.example/sites/all/_layouts/15/guestaccess.aspx?guestaccesstoken=Q4kdpx392MWTZ8RhbyN1Ka7m%2BTcqLwej5spK%2FmUnRQV%3D&folderid=2_7c31d90e24a815f96d02b4613e907a2fc&rev=1&e=9b271cd044716392c5207a44de8117a3
- 2) A surprising but human, clear, simple, white, lightning look!
- 3) WORDPRESS version so that I can edit easily and add text on existing and new pages
- We therefore pass each option and - even more so - through the sieve of this inevitable - and values-generating - ethical evaluation.
- In other words, we are doubly satisfied with EVERY solution:
- 1. As a DPO/consultant and advisor to commercial enterprises or non-profit organisations but necessarily entering into a relationship involving financial flows with the persons concerned; and
- 2. As concerned person: target of the actions envisaged, parent, child, citizen and avatar in our digital lives.
- We put personal data at the centre of our projects and internal meetings, and with clients, we therefore continue the stage of brainstorming, researching and visualising ideas in interaction with the Regulation, by analysing the ethical consequences of each option.
- We choose only solutions that are applicable to the greatest number and therefore satisfy us as citizens of an increasingly connected and digital world. We also see the Regulation as a commercial and marketing opportunity to enhance the value of personal data and develop the confidence of those concerned by respect and security in the processing of such data.
- Our ultimate test: we put ourselves in our children's shoes to test the option considered, then comment on it and evaluate it as a parent.
- NO TO INCOMPREHENSIVE LEGAL TERMS... It is simply prohibited from 25 May for all information to be communicated to the persons concerned by the Regulation!
Nice to have
- - Artificial Intelligence
- - Transhumans
- - Challenges becoming Opportunities
- - a Great Dame who Protects & Reassures (see GDPR logo)
- - Friendly communication - NOT too businesslike/cold/usual
- - Page content is available here in FRENCH then ENGLISH then DUTCH then GERMAN : https://files.pelmora.example/sh/k3j4h5g6f7d8s9a/AAV5fGhIjKlMnOpQrStUvWxY?dl=0
Should not have
- A cold, bankerlike, old economy, dull outlook

```html
<!DOCTYPE html>
<html lang="en">
<head>
<meta charset="utf-8">
<title>KTV — Welcome</title>
<link rel="stylesheet" href="https://fonts.googleapis.com/css2?family=Lato:wght@400;700;900&display=swap">
<style>
:root{
  --magenta:#c2378f;
  --magenta-deep:#b42f86;
  --pink:#d9519c;
  --peach:#f7b58e;
  --ink:#222226;
  --body:#4a4a50;
  --muted:#f1f1f1;
  --footer:#eeeeee;
  --white:#ffffff;
}
*{box-sizing:border-box;margin:0;padding:0}
html,body{width:1200px;height:3482px;overflow:hidden;background:var(--white)}
body{font-family:'Lato',sans-serif;color:var(--body);position:relative}
.abs{position:absolute}
.brand{display:flex;align-items:center;gap:12px;font-family:'Lato',sans-serif;font-weight:900;font-size:30px;color:var(--magenta);letter-spacing:1px}
.brand-dot{width:34px;height:34px;border-radius:50%;background:var(--magenta)}

/* header */
.site-header{left:0;top:0;width:1200px;height:128px;background:var(--white)}
.site-header .brand{position:absolute;left:74px;top:40px}
.nav{position:absolute;top:58px;left:0;width:1200px;list-style:none}
.nav li{position:absolute;font-size:15px;font-weight:700;color:var(--ink);letter-spacing:.3px;white-space:nowrap}
.nav li.active{color:var(--magenta)}

/* hero */
.hero{left:0;top:128px;width:1200px;height:517px;background:radial-gradient(ellipse at 72% 45%,#2b6fb8 0%,#12315e 35%,#0a1326 65%,#08090f 100%)}
.hero-title{left:74px;top:312px;font-size:36px;font-weight:900;color:var(--peach);letter-spacing:.5px}
.hero-sub{left:74px;top:370px;width:520px;font-size:23px;line-height:33px;color:var(--white)}
.hero-dots{left:74px;top:584px;display:flex;gap:10px}
.hero-dots span{width:10px;height:10px;border-radius:50%;background:var(--white)}
.hero-dots span.on{background:var(--pink)}

/* common */
.section-title{width:1200px;left:0;text-align:center;font-size:29px;font-weight:900;color:var(--ink);letter-spacing:.5px}
.lead{width:1200px;left:0;text-align:center;font-size:13.5px;color:var(--body)}
.btn{display:flex;align-items:center;justify-content:center;width:150px;height:46px;background:linear-gradient(90deg,var(--magenta) 0%,var(--peach) 100%);color:var(--white);font-size:13px;font-weight:900;letter-spacing:.6px}

/* welcome */
.welcome-text{left:79px;top:742px;width:1042px;text-align:center;font-size:13.5px;line-height:28px}

/* services */
.services{left:0;top:961px;width:1200px;height:302px;background:linear-gradient(100deg,var(--magenta-deep) 0%,var(--pink) 60%,#c8418f 100%)}
.services .section-title{color:var(--white);top:40px}
.service{position:absolute;top:98px;width:340px;text-align:center;color:var(--white)}
.service svg{display:block;margin:0 auto 12px}
.service h3{font-size:17px;font-weight:900;letter-spacing:.4px;margin-bottom:8px}
.service p{font-size:13.5px;line-height:22px;color:#f7d3e6;padding:0 40px}

/* steps */
.step-circle{width:190px;height:190px;border-radius:50%;background:linear-gradient(145deg,#f6c4b0 0%,var(--magenta) 40%,var(--magenta-deep) 100%);box-shadow:0 6px 18px rgba(0,0,0,.18);display:flex;align-items:center;justify-content:center}
.step-label{font-size:21px;color:var(--ink);letter-spacing:.5px}
.step-title{font-size:21px;font-weight:900;color:var(--magenta);letter-spacing:.4px}
.step-body{font-size:13.5px;line-height:27px;color:var(--body)}
.step-body ol{padding-left:34px}
.step-body ol li{padding-left:6px}
.feature{position:absolute;width:330px}
.feature h4{position:absolute;left:81px;top:0;font-size:13.5px;font-weight:900;color:var(--magenta);white-space:nowrap}
.feature p{position:absolute;left:81px;top:24px;width:260px;font-size:13.5px;line-height:25px}
.feature svg{position:absolute;left:0;top:8px}

/* what we do */
.what{left:0;top:2360px;width:613px;height:425px;background:var(--muted)}
.what h2{position:absolute;left:77px;top:68px;font-size:29px;font-weight:900;color:var(--ink)}
.what p{position:absolute;left:77px;top:118px;width:500px;font-size:13.5px;line-height:27px}
.what .btn{position:absolute;left:77px;top:300px}
.what-photo{left:613px;top:2360px;width:587px;height:425px;background:radial-gradient(ellipse at 60% 55%,#c87468 0%,#5a2630 30%,#1b1420 65%,#0a0a0e 100%)}

/* blog */
.post{position:absolute;top:2945px;width:330px}
.post-photo{width:330px;height:193px}
.post h3{margin-top:25px;font-size:17px;font-weight:900;color:var(--magenta);letter-spacing:.3px}
.post p{margin-top:8px;font-size:13.5px;line-height:24px}

/* footer */
.footer{left:0;top:3296px;width:1200px;height:186px;background:var(--footer);overflow:hidden}
.footer .brand{position:absolute;left:77px;top:44px}
.copy{position:absolute;left:77px;top:116px;font-size:12.5px;line-height:22px;color:var(--ink)}
.follow{position:absolute;left:689px;top:66px;font-size:12px;font-weight:700;color:var(--ink);letter-spacing:.5px}
.socials{position:absolute;left:689px;top:94px;display:flex;gap:14px}
.socials span{width:18px;height:18px;border-radius:50%;background:#3a3a3e}
.partner{position:absolute;left:944px;top:64px;font-family:'Lato',sans-serif;font-weight:700;font-size:28px;color:#3f4f7a;display:flex;align-items:center;gap:12px}
.partner i{display:block;width:34px;height:34px;border-radius:50%;background:#3f4f7a}
</style>
</head>
<body>

<header class="abs site-header">
  <div class="brand"><span class="brand-dot"></span>KTV</div>
  <ul class="nav">
    <li class="active" style="left:487px">HOME</li>
    <li style="left:573px">ABOUT US</li>
    <li style="left:687px">SERVICES</li>
    <li style="left:796px">HOW IT WORKS</li>
    <li style="left:952px">BLOG</li>
    <li style="left:1031px">CONTACT US</li>
  </ul>
</header>

<section class="abs hero" role="img" aria-label="Digital human profile formed by glowing network lines and data points"></section>
<h1 class="abs hero-title">WELCOME TO KTV</h1>
<p class="abs hero-sub">Lanventore veritatis et quasi architecto beatae vitae dicta sunt explicabo..</p>
<div class="abs hero-dots"><span class="on"></span><span></span><span></span><span></span></div>

<h2 class="abs section-title" style="top:690px">WELCOME TO OUR WEBSITE</h2>
<p class="abs welcome-text">Lorem ipsum dolor sit amet, consectetur adipisicing elit, sed do eiusmod tempor incididunt ut labore et doloreasdes magna aliqua. Ut enim ad minim veniam, quis nostrud exercitation ullamco laboris nisi ut aliquip ex ea commodalo consequat. Duis aute irure dolor in reprehenderit in voluptate velit esse cillum dolore eu fugiat nulla pariatur. Excepteur sint occaecat cupidatat non proident, sunt in culpa qui officia deserunt mollit anim id est laborum.</p>
<a class="abs btn" style="left:525px;top:854px">READ MORE</a>

<section class="abs services">
  <h2 class="abs section-title">OUR SERVICES</h2>
  <div class="service" style="left:71px">
    <svg width="56" height="64" viewBox="0 0 56 64" fill="none" stroke="#fff" stroke-width="2.5"><path d="M6 3h30l14 14v44H6z"/><path d="M36 3v14h14"/><path d="M14 26h26M14 34h26M14 42h18"/><path d="M14 53c4-4 6 3 10-1s6 2 10-1"/></svg>
    <h3>LEGAL DESIGN</h3>
    <p>Duis aute irure dolor in reprehenderit in voluptate velit esse cillum</p>
  </div>
  <div class="service" style="left:429px">
    <svg width="64" height="64" viewBox="0 0 64 64" fill="none" stroke="#fff" stroke-width="2.5"><circle cx="32" cy="32" r="26"/><circle cx="32" cy="32" r="5"/><circle cx="18" cy="22" r="3"/><circle cx="46" cy="22" r="3"/><circle cx="20" cy="44" r="3"/><circle cx="44" cy="44" r="3"/><path d="M21 23l7 6M43 23l-7 6M22 42l6-6M42 42l-6-6"/></svg>
    <h3>ARTIFICIAL INTELLIGENCE</h3>
    <p>Duis aute irure dolor in reprehenderit in voluptate velit esse cillum</p>
  </div>
  <div class="service" style="left:789px">
    <svg width="64" height="64" viewBox="0 0 64 64" fill="none" stroke="#fff" stroke-width="2.5"><rect x="8" y="8" width="48" height="48" rx="10"/><path d="M24 16c16 8-16 24 0 32M40 16c-16 8 16 24 0 32"/><path d="M27 24h10M27 40h10"/></svg>
    <h3>HUMAN BY DESIGN</h3>
    <p>Duis aute irure dolor in reprehenderit in voluptate velit esse cillum</p>
  </div>
</section>

<h2 class="abs section-title" style="top:1298px">OUR 3 STEPS</h2>
<p class="abs lead" style="top:1360px">Lorem ipsum dolor sit amet, consectetur adipisicing elit, sed do eiusmod tempor incididunt ut labore et doloreasdes magna aliqua.</p>

<!-- step 1 -->
<div class="abs step-circle" style="left:146px;top:1425px">
  <svg width="90" height="80" viewBox="0 0 90 80" fill="none" stroke="#fff" stroke-width="3.5"><rect x="6" y="6" width="70" height="50" rx="3"/><path d="M30 70h24M42 56v14"/><path d="M30 44l40-32 6 6-40 32-9 3z"/></svg>
</div>
<p class="abs step-label" style="left:378px;top:1420px">STEP 1:</p>
<h3 class="abs step-title" style="left:378px;top:1458px">GRAPHIC TABLE &amp; INTERACTION</h3>
<div class="abs step-body" style="left:378px;top:1500px;width:720px">
  The 3 profiles of our teams (IT/cybersecurity Expert - Lawyer - Project Manager) make use of<br>modern tools of communication INTERNALLY and EXTERNALLY: with external clients<br>and partners.<br>We use tactile tablets and graphic applications for drawing, mind-mapping, visualization, advanced<br>natural language generation (advanced NLG), video, storytelling,...
</div>

<!-- step 2 -->
<p class="abs step-label" style="left:144px;top:1717px">STEP 2:</p>
<h3 class="abs step-title" style="left:144px;top:1758px">HUMAN BY DESIGN</h3>
<div class="abs step-body" style="left:144px;top:1796px;width:640px">
  EACH solution passes a double test that satisfies us both :
  <ol>
    <li>As a DPO/consultant and advisor to commercial enterprises or non-profit organizations but necessarily entering into a relationship involving financial flows with the persons concerned;</li>
    <li>As a data subject : "target" of the envisaged actions, parent, child, citizen and avatar in our digital lives.</li>
  </ol>
</div>
<div class="abs step-circle" style="left:873px;top:1657px">
  <svg width="80" height="80" viewBox="0 0 80 80" fill="none" stroke="#fff" stroke-width="3.5"><rect x="10" y="10" width="60" height="60" rx="14"/><path d="M30 20c20 10-20 30 0 40M50 20c-20 10 20 30 0 40"/><path d="M33 30h14M33 50h14"/></svg>
</div>

<!-- step 3 -->
<div class="abs step-circle" style="left:146px;top:2017px">
  <svg width="90" height="80" viewBox="0 0 90 80" fill="none" stroke="#fff" stroke-width="3.5"><rect x="6" y="6" width="78" height="52" rx="3"/><path d="M32 72h26M45 58v14"/><path d="M16 48l18-20 12 12 8-8 16 16"/><circle cx="60" cy="22" r="5"/></svg>
</div>
<p class="abs step-label" style="left:378px;top:2014px">STEP 3:</p>
<h3 class="abs step-title" style="left:378px;top:2050px">VISUALIZATION AND REDACTION</h3>
<div class="abs step-body" style="left:378px;top:2092px;width:625px">
  During the first two stages, we prepared a desirable objective: Communicate visually after an ethical check. Two external solutions (human and artificial) will help us to finalize the communication in a professional and optimal way:
</div>
<div class="feature" style="left:378px;top:2201px">
  <svg width="50" height="48" viewBox="0 0 44 44" fill="none" stroke="#222" stroke-width="2"><rect x="3" y="4" width="38" height="28" rx="2"/><path d="M16 40h12M22 32v8"/><path d="M10 26V16M16 26V12M22 26V18M28 26V14M34 26V20"/></svg>
  <h4>GRAPHIC DESIGN OUTSOURCING</h4>
  <p>Just as electricity has transformed one industrial sector after another there is so much to be done</p>
</div>
<div class="feature" style="left:772px;top:2201px">
  <svg width="50" height="48" viewBox="0 0 44 44" fill="none" stroke="#222" stroke-width="2"><rect x="11" y="11" width="22" height="22" rx="3"/><rect x="17" y="17" width="10" height="10"/><path d="M16 5v6M22 5v6M28 5v6M16 33v6M22 33v6M28 33v6M5 16h6M5 22h6M5 28h6M33 16h6M33 22h6M33 28h6"/></svg>
  <h4>ARTIFICIAL INTELLIGENCE</h4>
  <p>Just as electricity has transformed one industrial sector after another there is so much to be done</p>
</div>

<!-- what we do -->
<section class="abs what">
  <h2>WHAT WE DO</h2>
  <p>Lorem ipsum dolor sit amet, consectetur adipisicing elit, sed do eiusmod tempor incididunt ut labore et doloreasdes magna aliqua. Ut enim ad minim veniam, quis nostrud exercitation ullamco laboris nisi ut aliquip ex ea commodalo consequat. Duis aute irure dolor in reprehenderit in voluptate velit esse cillum dolore eu fugiat nulla pariatur.</p>
  <a class="btn">READ MORE</a>
</section>
<div class="abs what-photo" role="img" aria-label="Robotic hand and human hand reaching toward each other against a dark background"></div>

<!-- blog -->
<h2 class="abs section-title" style="top:2830px">BLOG POSTS</h2>
<p class="abs lead" style="top:2892px">Lorem ipsum dolor sit amet, consectetur adipisicing elit, sed do eiusmod tempor incididunt ut labore et doloreasdes magna aliqua.</p>
<article class="post" style="left:77px">
  <div class="post-photo" role="img" aria-label="Glowing artificial intelligence network graphic with connected icons" style="background:radial-gradient(ellipse at 50% 50%,#d9e6f5 0%,#4f8fc8 25%,#1d4f6a 55%,#16261e 100%)"></div>
  <h3>LOREM IPSUM DOLOR SIT AMET</h3>
  <p>Adipisicing elit, sed do eiusmod tempor incididunt ut labore et doloreasdes magna aliqua magni dolores eos qui ratione...</p>
</article>
<article class="post" style="left:436px">
  <div class="post-photo" role="img" aria-label="Digital head silhouette built from glowing circuit points" style="background:radial-gradient(ellipse at 45% 50%,#e0a14a 0%,#3a5f9a 35%,#0f2450 70%,#081230 100%)"></div>
  <h3>LOREM IPSUM DOLOR SIT AMET</h3>
  <p>Adipisicing elit, sed do eiusmod tempor incididunt ut labore et doloreasdes magna aliqua magni dolores eos qui ratione...</p>
</article>
<article class="post" style="left:796px">
  <div class="post-photo" role="img" aria-label="Blue digital brain above a circuit board" style="background:radial-gradient(ellipse at 50% 40%,#b9cde6 0%,#5a7fa8 30%,#223c5e 65%,#111d30 100%)"></div>
  <h3>LOREM IPSUM DOLOR SIT AMET</h3>
  <p>Adipisicing elit, sed do eiusmod tempor incididunt ut labore et doloreasdes magna aliqua magni dolores eos qui ratione...</p>
</article>

<!-- footer -->
<footer class="abs footer">
  <svg class="abs" style="left:0;top:0" width="1200" height="186" viewBox="0 0 1200 186" fill="none"><path d="M0 40 C300 0 700 70 1200 20" stroke="#e4e4e4" stroke-width="2"/><path d="M0 150 C400 110 800 190 1200 130" stroke="#e6e6e6" stroke-width="2"/></svg>
  <div class="brand"><span class="brand-dot"></span>KTV</div>
  <p class="copy">Copyright © 2018 Company Name.<br>All Rights Reserved.</p>
  <p class="follow">FOLLOW US</p>
  <div class="socials"><span></span><span></span><span></span><span></span><span></span></div>
  <div class="partner"><i></i>ORLAX</div>
</footer>

</body>
</html>
```